Paper and board wholesaler needs business card design for managers

We need a business card design that incorporates bordo red, white and/ or grey colors. The business card has to have our "VELON" logo and our partners paper group logo that we are part of - "ROSKU group". Both of the logos should be applied to the business card according to the guidelines for the usage of the logo that have been added in the uploaded files.
The letters (information on the card) should be easily readable, so no "shiny" or "glossy" text.
Besides the two logos, the business card needs to contain information for the respective person:
1) Name, Surname,
2) Job position (e.g. "sales represantative"),
3) E-mail,
4) Phone number,
5) text: "Kartonu Mājvieta (VELON)" LTD
6) our office address "Riga, Sārtaines street 42".
(also could have) 7) our homepage address "www.velon.lv"
Holiday season, so have a lot of tasks to take care of and not as much time to check SketchHarbor as often.
1) Name, Surname, 2) Job position (e.g. "sales represantative"), 3) E-mail, 4) Phone number, 5) text: "Kartonu Mājvieta (VELON)" LTD 6) our office address "Riga, Sārtaines street 42". (also could have) 7) our homepage address "www.velon.lv"
Other font styles liked:
- Josefin Sans

```html
<!DOCTYPE html>
<html lang="en">
<head>
<meta charset="utf-8">
<title>VELON Business Card</title>
<link rel="stylesheet" href="https://fonts.googleapis.com/css2?family=Montserrat:wght@400;500;600;700&display=swap">
<style>
  :root {
    --bordo: #832f35;
    --bordo-light: #93393f;
    --bordo-dark: #76292f;
    --white: #ffffff;
    --ink: #1f1f1f;
    --green: #1f8a5b;
    --backdrop: #e4e4e4;
  }
  * { box-sizing: border-box; margin: 0; padding: 0; }
  html, body {
    width: 1200px; height: 1200px; overflow: hidden;
    background: var(--backdrop);
    font-family: "Montserrat", sans-serif;
  }
  .card {
    position: absolute; left: 160px;
    width: 880px; height: 519px;
    background: var(--white);
  }
  .card--front { top: 62px; }
  .card--back { top: 624px; }

  .brand { position: absolute; display: flex; align-items: center; }
  .brand__square { border: 4px solid currentColor; }
  .brand__name {
    font-weight: 500; letter-spacing: 0.85em; line-height: 1;
  }
  .card--front .brand { left: 171px; top: 65px; color: var(--bordo); }
  .card--front .brand__square { width: 98px; height: 129px; }
  .card--front .brand__name { font-size: 44px; margin-left: 80px; }

  .person { position: absolute; left: 0; right: 0; top: 248px; text-align: center; }
  .person__name {
    color: var(--bordo); font-weight: 600; font-size: 50px; letter-spacing: 0.02em; line-height: 1;
  }
  .person__role { color: var(--ink); font-size: 20px; margin-top: 12px; letter-spacing: 0.03em; }

  .contact-band { position: absolute; left: 0; top: 353px; width: 880px; height: 127px; }
  .contact-band svg.band-shape { position: absolute; inset: 0; }
  .contact-list { position: absolute; list-style: none; color: var(--white); font-size: 19px; }
  .contact-list li { display: flex; align-items: center; position: absolute; white-space: nowrap; }
  .contact-list svg { width: 15px; height: 15px; margin-right: 10px; fill: var(--white); }
  .contact-list--left { left: 92px; top: 0; }
  .contact-list--left li:nth-child(1) { top: 22px; }
  .contact-list--left li:nth-child(2) { top: 55px; }
  .contact-list--left li:nth-child(3) { top: 88px; }
  .contact-list--right { left: 536px; top: 0; }
  .contact-list--right li:nth-child(1) { top: 40px; }
  .contact-list--right li:nth-child(2) { top: 79px; }

  .card--back .brand-band {
    position: absolute; left: 0; top: 71px; width: 564px; height: 181px; background: var(--bordo);
  }
  .card--back .brand { left: 70px; top: 40px; color: var(--white); }
  .card--back .brand__square { width: 80px; height: 100px; }
  .card--back .brand__name { font-size: 36px; margin-left: 60px; }

  .partner {
    position: absolute; left: 374px; top: 368px;
    display: flex; align-items: center; color: var(--green);
  }
  .partner__circle { width: 92px; height: 92px; border: 5px solid currentColor; border-radius: 50%; }
  .partner__name { font-weight: 700; font-size: 52px; margin-left: 22px; letter-spacing: 0.01em; }
</style>
</head>
<body>

<section class="card card--front">
  <div class="brand">
    <span class="brand__square"></span>
    <span class="brand__name">VELON</span>
  </div>

  <div class="person">
    <h1 class="person__name">DANIEL ROWEN</h1>
    <p class="person__role">Owner</p>
  </div>

  <div class="contact-band">
    <svg class="band-shape" width="880" height="127" viewBox="0 0 880 127">
      <path d="M0 0H390L411 12V115L390 127H0Z" fill="var(--bordo)"/>
      <path d="M390 0L411 12V115L390 127Z" fill="var(--bordo-dark)"/>
      <path d="M411 12L434 0V127L411 115Z" fill="var(--bordo-light)"/>
      <path d="M434 0H880V127H434Z" fill="var(--bordo)"/>
    </svg>

    <ul class="contact-list contact-list--left">
      <li><svg viewBox="0 0 24 24"><path d="M6.6 10.8c1.4 2.8 3.8 5.1 6.6 6.6l2.2-2.2c.3-.3.7-.4 1-.2 1.1.4 2.3.6 3.6.6.6 0 1 .4 1 1V20c0 .6-.4 1-1 1C10.6 21 3 13.4 3 4c0-.6.4-1 1-1h3.5c.6 0 1 .4 1 1 0 1.3.2 2.5.6 3.6.1.3 0 .7-.2 1z"/></svg>(+371) 60 412 587</li>
      <li><svg viewBox="0 0 24 24"><path d="M2 5h20v14H2z M2 5l10 8 10-8" fill="var(--white)"/><path d="M3 6l9 7 9-7" fill="none" stroke="var(--bordo)" stroke-width="1.6"/></svg>info@velon.lv</li>
      <li><svg viewBox="0 0 24 24"><circle cx="12" cy="12" r="10"/><path d="M2 12h20M12 2c3 3 3 17 0 20M12 2c-3 3-3 17 0 20" fill="none" stroke="var(--bordo)" stroke-width="1.4"/></svg>www.velon.lv</li>
    </ul>

    <ul class="contact-list contact-list--right">
      <li>@KartonuMājvieta</li>
      <li><svg viewBox="0 0 24 24"><path d="M12 2a6 6 0 0 0-6 6c0 4.5 6 10 6 10s6-5.5 6-10a6 6 0 0 0-6-6zm0 8.5A2.5 2.5 0 1 1 12 5.5a2.5 2.5 0 0 1 0 5z"/><rect x="5" y="19.5" width="14" height="2"/></svg>Riga, Sārtaines street 42</li>
    </ul>
  </div>
</section>

<section class="card card--back">
  <div class="brand-band">
    <div class="brand">
      <span class="brand__square"></span>
      <span class="brand__name">VELON</span>
    </div>
  </div>

  <div class="partner">
    <span class="partner__circle"></span>
    <span class="partner__name">ROSKU group</span>
  </div>
</section>

</body>
</html>
```